Business Card for Technology Startup

Design a 2-sided business card using the logo provided. We are a digital healthcare platform that provides a mobile app and web UI that helps caregivers, families, and doctors share information and provide better patient outcomes. We use AI and machine learning to help guide patients through their day-to-day life. The final design should communicate stability, peace, comfort, but also align with the image of an AI-driven technology startup.

I'd like the deliverable to by a Photoshop PSD file (with layers) that I can work with in pixlr.com. Should contain the following editable layers:
Name (ex. Mara Quell)
Title (ex. Co-Founder / COO)
Email (ex. info@brenvaxa.ai)
Phone (ex. (555) 210-4478)
Website (ex. https://brenvaxa.ai)

```html
<!DOCTYPE html>
<html lang="en">
<head>
<meta charset="utf-8">
<title>Brenvaxa Business Card – Two Sides</title>
<link href="https://fonts.googleapis.com/css2?family=Poppins:wght@400;600;700&display=swap" rel="stylesheet">
<style>
  :root {
    --stage-blue: #035c96;
    --footer-grey: #999999;
    --label-grey: #9a9a9a;
    --card-white: #ffffff;
    --ink: #0a0a0a;
    --aqua-deep: #0ab4e8;
    --aqua-bright: #00fcff;
    --aqua-gradient: linear-gradient(90deg, var(--aqua-deep), var(--aqua-bright));
  }
  * { box-sizing: border-box; margin: 0; padding: 0; }
  html, body {
    width: 1200px; height: 1200px; overflow: hidden;
    background: var(--stage-blue);
    font-family: "Poppins", sans-serif;
  }
  .stage { position: relative; width: 1200px; height: 1200px; }

  .card {
    position: absolute; left: 307px; width: 586px; height: 360px; overflow: hidden;
  }
  .card--front { top: 204px; background: var(--card-white); }
  .card--back { top: 635px; background: var(--aqua-gradient); }

  .dot { position: absolute; border-radius: 50%; background: var(--aqua-gradient); }
  .dot--corner { left: -55px; top: -17px; width: 110px; height: 110px; }
  .dot--float { left: 204px; top: 41px; width: 112px; height: 112px; }
  .dot--low { left: 73px; top: 306px; width: 112px; height: 112px; }
  .dot--soft { box-shadow: -6px 4px 14px rgba(10, 150, 210, 0.25); }
  .dot--back-top { left: 73px; top: -56px; width: 112px; height: 112px; }
  .dot--back-side { left: -55px; top: 79px; width: 112px; height: 112px; }

  .contact {
    position: absolute; right: 56px; top: 69px; text-align: right; color: var(--ink);
  }
  .contact__name { font-weight: 600; font-size: 20px; line-height: 1.15; }
  .contact__title { font-size: 14px; line-height: 1.4; }
  .contact__lines { margin-top: 11px; font-size: 14px; line-height: 1.55; }

  .brand {
    position: absolute; right: 56px; display: flex; align-items: center; gap: 12px;
    color: var(--ink); font-weight: 700; line-height: 1;
  }
  .brand__dot { border-radius: 50%; flex: none; }
  .card--front .brand { top: 243px; font-size: 42px; }
  .card--front .brand__dot { width: 20px; height: 20px; background: var(--aqua-gradient); }
  .card--back .brand { top: 228px; font-size: 46px; }
  .card--back .brand__dot { width: 22px; height: 22px; background: var(--ink); }

  .website {
    position: absolute; right: 56px; top: 292px; font-size: 19px; color: var(--ink);
  }

  .side-label {
    position: absolute; left: 927px; display: flex; align-items: center; gap: 16px;
    color: var(--label-grey); font-size: 27px; letter-spacing: 0.5px;
  }
  .side-label--front { top: 366px; }
  .side-label--back { top: 797px; }

  .footer {
    position: absolute; left: 0; top: 1129px; width: 1200px; height: 71px;
    background: var(--footer-grey); color: #ffffff; font-size: 26px;
    display: flex; align-items: center; justify-content: flex-end; padding-right: 67px;
  }
</style>
</head>
<body>
<main class="stage">
  <section class="card card--front" aria-label="Card front">
    <div class="dot dot--corner"></div>
    <div class="dot dot--float"></div>
    <div class="dot dot--low"></div>
    <div class="contact">
      <p class="contact__name">Mara Quell</p>
      <p class="contact__title">Co-Founder / COO</p>
      <p class="contact__lines">info@brenvaxa.ai<br>(555) 210-4478</p>
    </div>
    <div class="brand"><span class="brand__dot"></span>brenvaxa</div>
  </section>

  <div class="side-label side-label--front">
    <svg width="22" height="24" viewBox="0 0 22 24" aria-hidden="true"><polygon points="0,12 22,0 22,24" fill="#9a9a9a"/></svg>
    SIDE 1
  </div>

  <section class="card card--back" aria-label="Card back">
    <div class="dot dot--soft dot--back-top"></div>
    <div class="dot dot--soft dot--back-side"></div>
    <div class="brand"><span class="brand__dot"></span>brenvaxa</div>
    <p class="website">www.brenvaxa.ai</p>
  </section>

  <div class="side-label side-label--back">
    <svg width="22" height="24" viewBox="0 0 22 24" aria-hidden="true"><polygon points="0,12 22,0 22,24" fill="#9a9a9a"/></svg>
    SIDE 2
  </div>

  <footer class="footer">Design 4</footer>
</main>
</body>
</html>
```